New business card design for Pinecrest Hollow Optometry Clinic

We need a new business card design using our existing logo (uploaded). Please do not include eyes, eye exam charts or beaches, water, sand. The logo I uploaded shows our colors of green and blue, but we are open to seeing it in black OR white. We would like to see something modern and fresh. It will need to be 2 sided. On the front we will need to be able to put a doctors name, for example-Dr Marta Kellerman and Associates. We will need to be able to change the name to other doctors names when we send for printing. The back of the card should list the following: 3817 Tarrow St, Fernwick Falls (P)705-555-0148 (E) info@phoc.ca www.phoc.ca. "We are welcoming new patients" and a line for the appointment date and time. I have uploaded the back of a card to give an example

```html
<!DOCTYPE html>
<html lang="en">
<head>
<meta charset="utf-8">
<title>Pinecrest Hollow Optometry Clinic – Business Card</title>
<link href="https://fonts.googleapis.com/css2?family=Montserrat:wght@700;800&family=Open+Sans:wght@400;600;800&display=swap" rel="stylesheet">
<style>
  :root {
    --brand-blue: #4660a9;
    --brand-green: #2ea55a;
    --paper: #ffffff;
    --backdrop: #262626;
  }
  * { box-sizing: border-box; margin: 0; padding: 0; }
  html, body { width: 1200px; height: 939px; overflow: hidden; }
  body {
    background: var(--backdrop);
    position: relative;
    font-family: "Open Sans", sans-serif;
  }
  .card {
    position: absolute;
    width: 540px;
    height: 310px;
    border-radius: 18px;
    background: var(--paper);
    overflow: hidden;
  }
  .card-front { left: 70px; top: 150px; }
  .card-back { left: 590px; top: 480px; }

  /* Front */
  .front-brand {
    position: absolute;
    left: 0; right: 0; top: 60px;
    display: flex; align-items: center; justify-content: center; gap: 18px;
  }
  .brand-dot {
    width: 54px; height: 54px; border-radius: 50%;
    background: var(--brand-green);
    flex: none;
  }
  .brand-name {
    font-family: "Montserrat", sans-serif;
    font-weight: 800;
    color: var(--brand-blue);
    font-size: 30px;
    line-height: 1.15;
  }
  .front-band {
    position: absolute;
    left: 0; right: 0; bottom: 0; height: 96px;
    background: var(--brand-blue);
  }
  .front-doctor {
    position: absolute; left: 0; right: 0; top: 26px;
    text-align: center; color: var(--paper);
    font-weight: 800; font-size: 19px;
  }

  /* Back */
  .back-shapes { position: absolute; inset: 0; }
  .back-brand {
    position: absolute; left: 36px; top: 40px; width: 160px;
    font-family: "Open Sans", sans-serif; font-weight: 800;
    color: var(--paper); font-size: 34px; letter-spacing: 1px;
    text-align: center;
  }
  .back-brand .brand-ring {
    display: block; width: 46px; height: 46px; margin: 0 auto 8px;
    border: 4px solid var(--paper); border-radius: 50%;
  }
  .contact-list {
    position: absolute; left: 250px; top: 22px;
    list-style: none; color: var(--paper);
    font-size: 15px; line-height: 21px; letter-spacing: 0.5px;
  }
  .contact-list li { display: flex; align-items: flex-start; gap: 10px; }
  .contact-list svg { width: 14px; height: 14px; margin-top: 4px; flex: none; }
  .contact-list .indent { padding-left: 24px; }
  .welcome {
    position: absolute; left: 18px; top: 155px;
    color: var(--paper); font-weight: 800; font-size: 19px; letter-spacing: 0.3px;
  }
  .appt-row {
    position: absolute; left: 36px; right: 28px;
    display: flex; align-items: flex-end; gap: 4px;
    color: var(--brand-green); font-size: 12px; letter-spacing: 0.5px;
  }
  .appt-row .fill { flex: 1; border-bottom: 2px dotted var(--brand-green); height: 1px; margin-bottom: 3px; }
  .appt-doctor { top: 215px; }
  .appt-date { top: 262px; }
</style>
</head>
<body>

<section class="card card-front" aria-label="Card front">
  <div class="front-brand">
    <span class="brand-dot"></span>
    <div class="brand-name">Pinecrest Hollow<br>Optometry Clinic</div>
  </div>
  <div class="front-band">
    <p class="front-doctor">Dr. Marta Kellerman &amp; Associates.</p>
  </div>
</section>

<section class="card card-back" aria-label="Card back">
  <svg class="back-shapes" viewBox="0 0 540 310" width="540" height="310" aria-hidden="true">
    <rect x="0" y="0" width="540" height="150" fill="var(--brand-blue)"/>
    <polygon points="0,150 398,150 376,188 0,188" fill="var(--brand-green)"/>
  </svg>

  <div class="back-brand"><span class="brand-ring"></span>PHOC</div>

  <ul class="contact-list">
    <li>
      <svg viewBox="0 0 14 14"><path d="M7 1a4 4 0 0 0-4 4c0 3 4 8 4 8s4-5 4-8a4 4 0 0 0-4-4zm0 5.5A1.5 1.5 0 1 1 7 3.5a1.5 1.5 0 0 1 0 3z" fill="#fff"/></svg>
      <span>3817 TARROW ST</span>
    </li>
    <li class="indent">FERNWICK FALLS</li>
    <li>
      <svg viewBox="0 0 14 14"><path d="M3 1.5l2 .5 1 3-1.5 1a7 7 0 0 0 3.5 3.5l1-1.5 3 1 .5 2c-.5 1-1.5 1.5-2.5 1.5A10 10 0 0 1 1.5 4C1.5 3 2 2 3 1.5z" fill="#fff"/></svg>
      <span>705-555-0148</span>
    </li>
    <li>
      <svg viewBox="0 0 14 14"><rect x="1" y="3" width="12" height="8" fill="#fff"/><path d="M1 3l6 4.5L13 3" stroke="var(--brand-blue)" stroke-width="1.2" fill="none"/></svg>
      <span>INFO@PHOC.CA</span>
    </li>
    <li>
      <svg viewBox="0 0 14 14"><circle cx="7" cy="7" r="6" fill="#fff"/><path d="M1 7h12M7 1c-3 3-3 9 0 12M7 1c3 3 3 9 0 12" stroke="var(--brand-blue)" stroke-width="1" fill="none"/></svg>
      <span>WWW.PHOC.CA</span>
    </li>
  </ul>

  <p class="welcome">WE ARE WELCOMING NEW PATIENTS!</p>

  <div class="appt-row appt-doctor">
    <span>DOCTOR:</span><span class="fill"></span>
    <span>TIME:</span><span class="fill"></span>
    <span>AM/PM</span>
  </div>
  <div class="appt-row appt-date">
    <span>DATE:</span><span class="fill"></span>
  </div>
</section>

</body>
</html>
```